"Aviation Law Firm Needs Banner for Fly-In Website"

My firm is looking for a web banner which will be advertised on www.skyrally-expo.org. The banner is going to be used for advertisement leading up to the big fly-in event being held in April.

My law firm represents pilots, plane owners, airlines, and anyone else that has an interest in aviation.

I would like to see some animation if possible, which would include aviation/cutting edge themes.

I would like to incorporate my logo and background images from my website (attached).

The advertisement should discretely near the firm name say "Offices: Lakeland"

The advertised words should be "Vectoring You Through Legal Turbulence"

The advertisement should also include my telephone number: "1-844-GRD-3097" and also my website "www.HangarCounselGroup.com"

The call to action should say "Contact Hangar Counsel Group"

This is a Vertical Ad and its dimensions are 300x600 PX (72 DPI)

Must be in PNG or JPEG format.

Target Market(s)

Pilots/Aviation Enthusiasts

Industry/Entity Type

Law Firm

Font styles to use
Serif
Sans Serif

Colors
fbf289
fbed22
ffffff
1b1b1b
000000

Requirements
Must have
• The banner should definitely look professional, yet cutting edge. The banner definitely needs those things listed in the project description.
Nice to have
• Animation

```html
<!DOCTYPE html>
<html lang="en">
<head>
<meta charset="utf-8">
<title>The Marlow Law Firm – Vertical Banners</title>
<link rel="stylesheet" href="https://fonts.googleapis.com/css2?family=Lora:wght@400;700&family=Tinos&display=swap">
<style>
  :root {
    --canvas: #ffffff;
    --sky-top: #8db4d3;
    --sky-mid: #5f9bc7;
    --cloud: #dfe3e6;
    --cabin: #e9d9c6;
    --white: #ffffff;
    --gold: #fbdc6e;
    --ink: #000000;
    --ink-soft: #1b1b1b;
    --faint: rgba(255,255,255,0.72);
  }
  * { margin: 0; padding: 0; box-sizing: border-box; }
  html, body { width: 1200px; height: 1200px; overflow: hidden; background: var(--canvas); }
  .canvas { position: relative; width: 1200px; height: 1200px; }
  .banner {
    position: absolute; top: 96px; width: 480px; height: 960px; overflow: hidden;
    text-align: center; font-family: "Lora", serif;
  }
  .banner--contact { left: 78px; }
  .banner--tagline { left: 636px; }
  .banner__scene {
    position: absolute; inset: 0;
    background:
      radial-gradient(ellipse 75% 40% at 50% 88%, var(--cloud) 0%, rgba(223,227,230,0) 100%),
      linear-gradient(180deg, var(--sky-top) 0%, var(--sky-mid) 45%, #7fb0d3 68%, var(--cloud) 82%, var(--cabin) 100%);
  }
  .banner__content { position: absolute; inset: 0; }
  .firm { position: absolute; top: 2px; left: 0; right: 0; color: var(--white); font-family: "Tinos", serif; font-variant: small-caps; }
  .firm__name { font-size: 45px; line-height: 52px; letter-spacing: 0.5px; }
  .firm__practice { font-size: 25px; line-height: 28px; margin-top: 2px; }
  .firm__practice .divider { display: inline-block; width: 2px; height: 20px; background: var(--white); margin: 0 14px; vertical-align: -2px; }
  .cta__lead { position: absolute; top: 170px; left: 0; right: 0; color: var(--white); font-weight: 700; font-size: 46px; }
  .cta__name { position: absolute; top: 240px; left: 0; right: 0; color: var(--gold); font-weight: 700; font-size: 52px; line-height: 90px; }
  .contact { position: absolute; top: 660px; left: 0; right: 0; }
  .contact__label { color: var(--ink); font-weight: 700; font-size: 43px; line-height: 50px; }
  .contact__phone { color: var(--ink); font-weight: 700; font-size: 43px; line-height: 50px; margin-top: 24px; }
  .contact__web { color: var(--ink-soft); font-size: 27px; line-height: 34px; margin-top: 8px; }
  .tagline { position: absolute; top: 128px; left: 0; right: 0; color: var(--white); font-weight: 700; font-size: 49px; line-height: 67px; }
  .office { position: absolute; top: 688px; left: 0; right: 0; padding-left: 10px; color: var(--faint); }
  .office__title { font-size: 36px; line-height: 44px; }
  .office__line { font-size: 27px; line-height: 34px; }
</style>
</head>
<body>
<div class="canvas">
  <section class="banner banner--contact">
    <div class="banner__scene" role="img" aria-label="View from an airplane window of a white wing with a red winglet above blue sky and clouds"></div>
    <div class="banner__content">
      <header class="firm">
        <div class="firm__name">The Marlow Law Firm</div>
        <div class="firm__practice">Aviation Law<span class="divider"></span>Dron Law</div>
      </header>
      <div class="cta__lead">Contact</div>
      <div class="cta__name">Hangar Counsel<br>Group</div>
      <div class="contact">
        <div class="contact__label">Call Toll-Free</div>
        <div class="contact__phone">1-844-GRD-3097</div>
        <div class="contact__web">www.HangarCounselGroup.com</div>
      </div>
    </div>
  </section>

  <section class="banner banner--tagline">
    <div class="banner__scene" role="img" aria-label="View from an airplane window of a white wing with a red winglet above clouds"></div>
    <div class="banner__content">
      <header class="firm">
        <div class="firm__name">The Marlow Law Firm</div>
        <div class="firm__practice">Aviation Law<span class="divider"></span>Dron Law</div>
      </header>
      <div class="tagline">Vectoring<br>You Through<br>Legal<br>Turbulence</div>
      <div class="office">
        <div class="office__title">Lakeland Offices</div>
        <div class="office__line">Address: P.O. Box 4170</div>
        <div class="office__line">Lakeland, FL 33805</div>
      </div>
    </div>
  </section>
</div>
</body>
</html>
```